Business card and Stationery for data intelligence company

We need a new design for our business cards and stationery (Business Letter templates and a Quote example on Word, but it MUST work on Google Doc as well).

We are a software company based in Ireland and UK. Our product is "Kovar", data intelligence platform with beautiful visualizations, graph capabilities (things are interconnected), powerful, flexible, it can manage Big Data and Streaming information. It's modern and relatively open source.
Our company will provide data intelligence for law enforcements, pharmaceuticals, and similar high end customers.

We'll launch a new website soon. At the moment it's http://www.kovar-analytics.example if you want to take a look. This is our youtube channel in case you need it to understand what Kovar is: https://www.youtube.com/c/kovaranalyticschannel

We changed the logo so please use the logo I attach here.

We'd like the output to be cool and modern but elegant and "business" at the same time. It should inspire simple sophistication, "unity" "intent" "purpose" yet subtly very advanced and innovative.

The name "Kovar" does NOT refer to sirens (mithological creatures) as well as the warning devices. It means Kinetic Object Vector Analysis Reactor. Please use our logo's colors and if you want to something like the "graph" image.

```html
<!DOCTYPE html>
<html lang="en">
<head>
<meta charset="utf-8">
<title>Kovar Data Intelligence – Business Card</title>
<link href="https://fonts.googleapis.com/css2?family=Montserrat:wght@400;500&family=Open+Sans:wght@400;600;700&display=swap" rel="stylesheet">
<style>
  :root {
    --backdrop-top: #4b4b4b;
    --backdrop-bottom: #5e5e5e;
    --brand-orange: #f9b03c;
    --brand-orange-deep: #f3a52c;
    --paper: #ffffff;
    --rule-grey: #b9b9b9;
    --tagline-grey: #9a9a9a;
    --ink: #333333;
  }
  * { margin: 0; padding: 0; box-sizing: border-box; }
  html, body { width: 1200px; height: 900px; overflow: hidden; }
  body {
    position: relative;
    background: linear-gradient(180deg, var(--backdrop-top), var(--backdrop-bottom));
    font-family: "Open Sans", Arial, sans-serif;
  }
  .card {
    position: absolute;
    top: 306px;
    width: 440px;
    height: 271px;
    border-radius: 11px;
    overflow: hidden;
    box-shadow: 0 2px 6px rgba(0,0,0,0.25);
  }
  .card-front { left: 149px; background: var(--brand-orange); }
  .card-back { left: 608px; background: var(--brand-orange); }

  /* Front */
  .front-header {
    position: absolute; left: 0; top: 0; width: 100%; height: 119px;
    background: var(--paper);
  }
  .front-rule {
    position: absolute; left: 0; top: 119px; width: 100%; height: 6px;
    background: var(--rule-grey);
  }
  .wordmark {
    font-family: "Montserrat", Arial, sans-serif;
    font-weight: 400;
    letter-spacing: 0.16em;
    line-height: 1;
  }
  .front-wordmark {
    position: absolute; left: 25px; top: 30px;
    font-size: 47px; color: var(--brand-orange);
  }
  .tagline {
    font-family: "Montserrat", Arial, sans-serif;
    font-weight: 400;
    letter-spacing: 0.27em;
    line-height: 1;
  }
  .front-tagline {
    position: absolute; left: 27px; top: 75px;
    font-size: 11.5px; color: var(--tagline-grey);
  }
  .holder {
    position: absolute; right: 26px; top: 42px; text-align: right;
  }
  .holder-name {
    font-weight: 700; font-size: 17px; color: var(--brand-orange); line-height: 1.1;
  }
  .holder-role {
    font-size: 12.5px; color: var(--ink); margin-top: 1px;
  }
  .contact-list {
    position: absolute; left: 28px; top: 144px; list-style: none;
    color: var(--paper); font-size: 12px; line-height: 16px;
  }
  .contact-list li { display: flex; align-items: center; gap: 9px; }
  .contact-list svg { width: 10px; height: 10px; flex: none; }
  .address {
    position: absolute; left: 27px; top: 214px;
    color: var(--paper); font-size: 12px; line-height: 16px;
  }
  .mark-ring {
    position: absolute; left: 290px; top: 128px;
  }

  /* Back */
  .back-field {
    position: absolute; inset: 0;
    background: radial-gradient(circle at 50% 40%, var(--brand-orange) 0%, var(--brand-orange-deep) 100%);
  }
  .back-mark {
    position: absolute; left: 176px; top: 42px;
  }
  .back-wordmark {
    position: absolute; left: 0; width: 100%; top: 140px; text-align: center;
    font-size: 50px; color: var(--paper); padding-left: 0.16em;
  }
  .back-tagline {
    position: absolute; left: 0; width: 100%; top: 184px; text-align: center;
    font-size: 12px; color: var(--paper); padding-left: 0.27em;
  }
  .social-band {
    position: absolute; left: 0; top: 216px; width: 100%; height: 34px;
    background: var(--paper);
    display: flex; justify-content: center; align-items: center; gap: 22px;
  }
  .social-handle {
    font-weight: 600; font-size: 11px; color: var(--brand-orange);
  }
</style>
</head>
<body>

<section class="card card-front" aria-label="Business card front">
  <div class="front-header"></div>
  <div class="front-rule"></div>
  <div class="wordmark front-wordmark">KOVAR</div>
  <div class="tagline front-tagline">DATA INTELLIGENCE</div>
  <div class="holder">
    <div class="holder-name">Daniel Brennan</div>
    <div class="holder-role">Managing Director</div>
  </div>

  <ul class="contact-list">
    <li>
      <svg viewBox="0 0 10 10"><path d="M1 3 Q5 0 9 3 L8 4.5 L6.5 3.8 L6.5 3 Q5 2.5 3.5 3 L3.5 3.8 L2 4.5 Z M2.5 5 H7.5 L8.5 9 H1.5 Z" fill="#fff"/></svg>
      123-456-7890
    </li>
    <li>
      <svg viewBox="0 0 10 10"><rect x="1" y="3" width="8" height="6" rx="1" fill="#fff"/><rect x="2.5" y="0.5" width="5" height="3" fill="#fff"/><rect x="3" y="5" width="4" height="1" fill="#f9b03c"/></svg>
      123-456-7890
    </li>
    <li>
      <svg viewBox="0 0 10 10"><rect x="0.5" y="2" width="9" height="6.5" rx="1" fill="#fff"/><path d="M1 2.5 L5 5.5 L9 2.5" stroke="#f9b03c" stroke-width="1" fill="none"/></svg>
      info@youremail.com
    </li>
    <li>
      <svg viewBox="0 0 10 10"><path d="M4 6 L6 4 M3.2 5 L1.8 6.4 a1.4 1.4 0 0 0 1.8 1.8 L5 6.8 M6.8 5 L8.2 3.6 a1.4 1.4 0 0 0 -1.8 -1.8 L5 3.2" stroke="#fff" stroke-width="1.1" fill="none" stroke-linecap="round"/></svg>
      www.yourweb.com
    </li>
  </ul>

  <div class="address">1234, Address Goes Here<br>Country Name, 123456</div>

  <svg class="mark-ring" width="140" height="140" viewBox="0 0 140 140" aria-hidden="true">
    <circle cx="69" cy="70" r="61" fill="none" stroke="#f3a52c" stroke-width="9"/>
  </svg>
</section>

<section class="card card-back" aria-label="Business card back">
  <div class="back-field" role="img" aria-label="Field of faint repeating brand motifs in orange"></div>
  <svg class="back-mark" width="88" height="88" viewBox="0 0 88 88" aria-hidden="true">
    <circle cx="44" cy="44" r="38" fill="none" stroke="#ffffff" stroke-width="8"/>
  </svg>
  <div class="wordmark back-wordmark">KOVAR</div>
  <div class="tagline back-tagline">DATA INTELLIGENCE</div>
  <div class="social-band">
    <span class="social-handle">Friendline</span>
    <span class="social-handle">Chirpnet</span>
    <span class="social-handle">Workgrid</span>
  </div>
</section>

</body>
</html>
```